Web Site for Strategy and Technology Consulting Company

We are looking for a website design that engages potential customers to understand our services and contact us. In this contest, we are looking for a homepage design, but the winning designer will be favored for the design of some of the more complicated interior pages of the site. An additional contest (or contests) for these pages will be added soon.

PLATROM AND RESPONSIVE DESIGN
The site will be implemented in WordPress using the Elementor page builder.
We are looking for a design that will look good on phones are well as laptop browsers.

UPLOADED FILES INCLUDE:
1a A wireframe of the homepage we are looking for. The Uploaded PDF also includes a draft of the text proposed for the homepage. Designers are free to go beyond the wireframe, but all elements of the wireframe should be included.
1b A Word document with the draft text of the homepage.
2a-d The Corvalin logo. Two versions are included – a dark version which works well against a light background, and a light version which works well against a dark background.
3 The Corvalin color palette with HEX and RGB values. Designers are not limited to this palette, but colors should be complementary.
4 A draft of the homepage menu
5 Service sheets with information on the services we provide

MORE ABOUT CORVALIN
Corvalin is a consulting company focused on transforming businesses through software. Our tagline, “Transformation Delivered,” recognizes the gap business often have between business transformation and the software they end up with. By listening to our customers and understanding their vision and where they are, we help get our customers where they want to go.

We increase our capability by working with many consultants and partners, allowing us to provide our customers with the best people and the software that best suits them.

Industry/Entity Type

Consulting

Number of Pages Required

1 page

Font styles to use
Sans Serif

Requirements
Must have
• the content represented on the wireframe uploaded
Nice to have
• interactive features, such as roll-over icons that reveal additional information

```html
<!DOCTYPE html>
<html lang="en">
<head>
<meta charset="utf-8">
<title>Corvalin — Transformation Delivered</title>
<link href="https://fonts.googleapis.com/css2?family=Poppins:wght@500;600;700;800&family=Montserrat:wght@400;500;600;700&display=swap" rel="stylesheet">
<style>
:root{
  --navy:#3b4a5e;
  --ink:#4a5566;
  --blue-deep:#1f5a91;
  --blue-mid:#3f6fc0;
  --blue-pale:#e2ebf6;
  --blue-soft:#7ea6cc;
  --yellow:#efb81b;
  --grey-btn:#a7b7c8;
  --grey-band:#eef0f3;
  --footer:#4b586d;
  --footer-dark:#3d4859;
  --white:#fff;
  --muted:#8592a3;
}
*{box-sizing:border-box;margin:0;padding:0}
html,body{width:1200px;height:4184px;overflow:hidden;background:#fff}
body{position:relative;font-family:"Montserrat",sans-serif;color:var(--ink);font-size:13px;line-height:1.5}
.abs{position:absolute}
h1,h2,h3,h4,.heading{font-family:"Poppins",sans-serif;color:var(--navy)}
.btn{position:absolute;display:flex;align-items:center;justify-content:center;border-radius:20px;font-family:"Poppins",sans-serif;font-weight:700;font-size:11px;letter-spacing:.3px;color:#fff;text-transform:uppercase}
.btn-grey{background:var(--grey-btn)}
.btn-yellow{background:var(--yellow)}

/* header */
.site-header{position:absolute;left:0;top:0;width:1200px;height:94px;border-bottom:1px solid #eceff3}
.brand{position:absolute;font-family:"Montserrat",sans-serif;font-weight:500;color:#8592a3;display:flex;align-items:center;gap:8px;line-height:1}
.brand .dot{width:10px;height:10px;background:var(--blue-deep);border-radius:50%}
.main-nav{position:absolute;left:540px;top:37px;display:flex;gap:22px;font-family:"Poppins",sans-serif;font-weight:600;font-size:12px;color:var(--navy);align-items:center}
.main-nav span::after{content:" ▾";font-size:8px}

/* hero */
.hero-title{left:86px;top:165px;font-size:58px;line-height:1.12;font-weight:800}
.hero-text{left:86px;top:302px;width:500px;font-size:13.5px;line-height:1.5}
.divider{left:86px;top:406px;width:228px;height:2px;background:#e3e6ea}
.ticks{left:86px;top:432px;width:500px;list-style:none;font-size:13px}
.ticks li{position:relative;padding-left:20px;margin-bottom:8px;line-height:1.45}
.ticks li::before{content:"";position:absolute;left:0;top:4px;width:11px;height:11px;border-radius:50%;background:var(--yellow)}
.ticks li::after{content:"";position:absolute;left:3px;top:6px;width:4px;height:3px;border-left:1.5px solid #fff;border-bottom:1.5px solid #fff;transform:rotate(-45deg)}
.illus{position:absolute}
.hero-illus{left:640px;top:150px;width:520px;height:480px;border-radius:52% 48% 44% 56%/50% 46% 54% 50%;background:linear-gradient(155deg,var(--blue-pale) 0%,#b9cdea 42%,var(--blue-mid) 100%)}
.people-illus{left:125px;top:1490px;width:520px;height:440px;border-radius:48% 52% 46% 54%/52% 48% 52% 48%;background:linear-gradient(200deg,var(--blue-pale) 0%,#b4c8e8 45%,var(--blue-mid) 100%)}

/* tech band */
.band-title{left:0;width:1200px;top:800px;text-align:center;color:#fff;font-size:33px;font-weight:700;line-height:1.25}
.band-text{left:255px;width:690px;top:895px;text-align:center;color:#fff;font-size:13.5px;line-height:1.5}
.services{left:88px;top:1005px;width:1024px;height:305px;display:flex;background:#fff;box-shadow:0 12px 30px rgba(40,60,90,.12)}
.service{flex:1;position:relative;text-align:center;padding-top:50px}
.service .icon{width:70px;height:70px;margin:0 auto 14px;border-radius:8px;background:linear-gradient(135deg,#e8eef5,#cddbe9)}
.service h3{font-size:12px;font-weight:600;line-height:1.35;color:var(--navy)}
.service p{font-size:11.5px;width:130px;margin:12px auto 0;line-height:1.4}
.service a{display:block;margin-top:14px;font-size:10.5px;font-weight:600;color:var(--muted);text-decoration:underline}
.chev{position:absolute;right:-22px;top:118px;width:0;height:0;border-top:34px solid transparent;border-bottom:34px solid transparent;border-left:22px solid;z-index:2}
.cta-line{left:0;width:1200px;top:1362px;text-align:center;font-size:13.5px}

/* people */
.people-title{left:666px;top:1525px;font-size:32px;font-weight:700}
.people-text{left:666px;width:420px;font-size:13px;line-height:1.5}

/* testimonials */
.section-title{left:0;width:1200px;text-align:center;font-size:32px;font-weight:700}
.testi{position:absolute;top:2095px;width:332px;height:201px;background:#fff;box-shadow:0 10px 28px rgba(40,60,90,.12);padding:66px 28px 0 30px}
.avatar{position:absolute;left:40px;top:-35px;width:72px;height:72px;border-radius:50%;background:linear-gradient(135deg,#b9a08f,#5d5149);border:3px solid #fff}
.quote-mark{position:absolute;left:195px;top:0;font-family:"Poppins",sans-serif;font-size:110px;line-height:1;color:#eef0f3;font-weight:800}
.testi p{position:relative;font-size:13px;line-height:1.55}
.testi .who{position:absolute;left:28px;right:28px;bottom:24px;display:flex;justify-content:space-between;align-items:center;font-family:"Poppins",sans-serif;font-weight:600;font-size:13.5px;color:var(--navy)}
.stars{color:var(--yellow);font-size:11px;letter-spacing:1px}
.arrow{position:absolute;top:2340px;width:48px;height:48px;border-radius:50%;display:flex;align-items:center;justify-content:center;color:#fff;font-weight:700;font-size:14px}

/* platforms */
.platforms{left:0;top:2474px;width:1200px;height:304px;background:var(--grey-band)}
.partner{position:absolute;top:2628px;display:flex;align-items:center;gap:6px;font-family:"Montserrat",sans-serif;font-weight:600;font-size:20px}
.partner i{display:block;width:16px;height:16px}
.dots{left:575px;top:2703px;display:flex;gap:10px}
.dots b{width:9px;height:9px;border-radius:50%;background:#c9ced6}
.dots b.on{background:var(--navy)}

/* blog */
.post{position:absolute;top:2932px;width:332px;height:430px;background:#fff;box-shadow:0 10px 28px rgba(40,60,90,.12)}
.post .photo{height:243px;background:linear-gradient(135deg,#2b3340,#6b7785 55%,#c7ccd2)}
.post h3{margin:28px 28px 0;font-size:15px;font-weight:700}
.post .meta{margin:14px 28px 0;font-size:10.5px;color:var(--muted);display:flex;gap:26px}
.post p{margin:14px 28px 0;font-size:13px;line-height:1.55}
.post a{display:block;margin:14px 28px 0;font-size:10.5px;font-weight:600;color:var(--muted);text-decoration:underline}

/* newsletter & footer */
.news{left:137px;top:3472px;width:925px;height:208px;background:var(--yellow);border-radius:104px}
.news h2{position:absolute;left:80px;top:60px;font-size:31px;font-weight:800;color:#fff}
.news p{position:absolute;left:80px;top:112px;width:420px;color:#fff;font-size:14px;line-height:1.3}
.email{position:absolute;left:550px;top:88px;width:320px;height:44px;background:#fff;border-radius:22px;display:flex;align-items:center;padding-left:44px;font-size:12px;color:var(--muted)}
.email .send{position:absolute;right:5px;top:5px;width:34px;height:34px;border-radius:50%;background:var(--grey-btn)}
.foot-col{position:absolute;top:3842px;color:#fff}
.foot-col h4{font-size:19px;font-weight:700;color:#fff;margin-bottom:20px}
.foot-col li{list-style:none;font-size:12px;margin-bottom:11px;color:#e8ecf1}
.foot-col li::before{content:"› ";}
.contact-item{position:relative;padding-left:22px;font-size:12px;color:#e8ecf1;margin-bottom:16px;line-height:1.45}
.contact-item svg{position:absolute;left:0;top:2px}
.socials{left:175px;top:3937px;display:flex;gap:14px}
.socials b{width:38px;height:38px;border-radius:50%;background:rgba(255,255,255,.22)}
.bottom-bar{left:0;top:4126px;width:1200px;height:58px;background:var(--footer-dark);color:#fff;text-align:center;font-size:12.5px;line-height:58px}
.chat{left:1134px;top:4100px;width:50px;height:50px;border-radius:50%;background:var(--yellow)}
</style>
</head>
<body>

<header class="site-header">
  <div class="brand" style="left:92px;top:27px;font-size:40px"><span class="dot"></span>Corvalin</div>
  <nav class="main-nav">
    <svg width="14" height="13" viewBox="0 0 14 13"><path d="M7 0L0 6h2v7h4V9h2v4h4V6h2z" fill="#a7b7c8"/></svg>
    <span>About Us</span><span>Services</span><span>Insights</span><span>Join Us</span>
  </nav>
  <div class="btn btn-yellow" style="left:980px;top:28px;width:130px;height:36px">Contact Us</div>
</header>

<!-- hero -->
<h1 class="abs hero-title">Transformation<br>Delivered</h1>
<p class="abs hero-text">We do more for our customers than implement software. We listen. We work to understand where they are in their transformation journey and where they want to go. We partner with them to clear the roadblocks that stand in their way, ensuring they reach their destination. At Corvalin, we:</p>
<div class="abs divider"></div>
<ul class="abs ticks">
  <li>Focus on business value, with an emphasis on delivering value quickly.</li>
  <li>Meet our customers where they are without backing them up to the beginning of their journey.</li>
  <li>Provide a wide range of services, from strategy to product support.</li>
  <li>Commit to our customer’s long-term success.</li>
</ul>
<p class="abs" style="left:86px;top:570px;font-size:13px">Corvalin is business transformation, delivered.</p>
<div class="btn btn-grey" style="left:88px;top:617px;width:133px;height:37px">Our Story</div>

<svg class="abs" style="left:0;top:590px" width="1200" height="520" viewBox="0 0 1200 520" aria-hidden="true">
  <defs><linearGradient id="bandGrad" x1="0" x2="1" y1="0" y2="0"><stop offset="0" stop-color="#1f5a91"/><stop offset="1" stop-color="#7ea6cc"/></linearGradient></defs>
  <path d="M0,40 C120,170 300,180 520,150 C760,115 1000,70 1200,20 L1200,515 L0,515 Z" fill="url(#bandGrad)"/>
</svg>
<div class="illus hero-illus" role="img" aria-label="Illustration of two consultants working with large dashboard screens and charts"></div>

<!-- technology band -->
<h2 class="abs band-title heading" style="color:#fff">Transformation<br>Supported by Technology</h2>
<p class="abs band-text">During our early years, Corvalin focused only on business transformation. We came to realize that successful transformation often depended on quality software implementations, and often more than one. Now we focus on five things, the five things most businesses need to reach their goals.</p>

<div class="abs services">
  <div class="service"><div class="icon" role="img" aria-label="Business transformation icon"></div><h3>Business<br>Transformation</h3><p>Define and execute your strategy.</p><a>VIEW DETAIL</a><span class="chev" style="color:var(--yellow)"></span></div>
  <div class="service"><div class="icon" role="img" aria-label="ERP icon"></div><h3>ERP<br>Implementations</h3><p>Assess, upgrade, and implement ERP.</p><a>VIEW DETAIL</a><span class="chev" style="color:var(--blue-deep)"></span></div>
  <div class="service"><div class="icon" role="img" aria-label="CRM icon"></div><h3>CRM<br>Implementations</h3><p>Take your relationships to the next level</p><a>VIEW DETAIL</a><span class="chev" style="color:#9ab5cf"></span></div>
  <div class="service"><div class="icon" role="img" aria-label="BI and data icon"></div><h3>BI and<br>Data</h3><p>Discover, connect, and trust your data.</p><a>VIEW DETAIL</a><span class="chev" style="color:#5f6b79"></span></div>
  <div class="service"><div class="icon" role="img" aria-label="Team building icon"></div><h3>Building the Right<br>Team of People</h3><p>Hire resources for your transformation journey.</p><a>VIEW DETAIL</a></div>
</div>
<p class="abs cta-line">Find out how Corvalin can help you put all the pieces together and get them done.</p>
<div class="btn btn-grey" style="left:530px;top:1398px;width:140px;height:37px">How We Work</div>

<!-- people -->
<div class="illus people-illus" role="img" aria-label="Illustration of two people beside a large video screen with charts"></div>
<h2 class="abs people-title">It’s the People</h2>
<p class="abs people-text" style="top:1578px">The world has changed in the past twenty years. The people you need might not all work for one company. Our clients want the best resources, available quickly. That’s why, in addition to our team of experts, we partner with:</p>
<ul class="abs ticks" style="left:666px;top:1677px;width:420px">
  <li>A large network of expert consultants who are the best at what they do,</li>
  <li>Service providers all over the world to provide the resources and value that are right for you, available 24 x 7.</li>
</ul>
<p class="abs people-text" style="top:1782px">People are invariably at the center of our customer’s success. Find out how we can add our experts to yours.</p>
<div class="btn btn-grey" style="left:668px;top:1848px;width:122px;height:36px">Out Team</div>

<!-- testimonials -->
<h2 class="abs section-title" style="top:1990px">Testimonials</h2>
<div class="testi" style="left:88px"><div class="avatar" role="img" aria-label="Client portrait"></div><span class="quote-mark">“</span><p>Aenean sollicitudin, lorem quis bibendum auctor, nisi elit consequat ipsum sagittis sem nibh id elit duis sed odio.</p><div class="who">Amara Desai<span class="stars">★★★★★</span></div></div>
<div class="testi" style="left:435px"><div class="avatar" role="img" aria-label="Client portrait"></div><span class="quote-mark">“</span><p>Aenean sollicitudin, lorem quis bibendum auctor, nisi elit consequat ipsum sagittis sem nibh id elit duis sed odio.</p><div class="who">Chloe Everett<span class="stars">★★★★★</span></div></div>
<div class="testi" style="left:780px"><div class="avatar" role="img" aria-label="Client portrait"></div><span class="quote-mark">“</span><p>Aenean sollicitudin, lorem quis bibendum auctor, nisi elit consequat ipsum sagittis sem nibh id elit duis sed odio.</p><div class="who">Caitlin Horne<span class="stars">★★★★★</span></div></div>
<div class="arrow" style="left:548px;background:var(--navy)">‹</div>
<div class="arrow" style="left:604px;background:var(--yellow)">›</div>

<!-- platforms -->
<div class="abs platforms"></div>
<h2 class="abs section-title" style="top:2543px">Platforms</h2>
<div class="partner" style="left:133px;color:#e8b21a"><i style="background:#e8b21a"></i>Lumetric</div>
<div class="partner" style="left:310px;color:#c8312b">Orvanta</div>
<div class="partner" style="left:462px;color:#4a5b76"><i style="background:#4a5b76;border-radius:50%"></i>Tabula</div>
<div class="partner" style="left:630px;color:#29a8e0"><i style="background:#29a8e0;border-radius:50%"></i>Frostline</div>
<div class="partner" style="left:805px;color:#1e5b9c">Dayforge</div>
<div class="partner" style="left:968px;color:#4b5563">Quorra<i style="background:#3aa655;border-radius:50%"></i></div>
<div class="abs dots"><b></b><b class="on"></b><b></b></div>

<!-- blog -->
<h2 class="abs section-title" style="top:2864px">Latest Blog</h2>
<article class="post" style="left:88px"><div class="photo" role="img" aria-label="Photo of hands typing at a laptop beside code screens"></div><h3>01: Some Blog Heading Here</h3><div class="meta"><span>▦ 25-05-2023</span><span>● By John</span></div><p>Aenean sollicitudin lorem quis bibendum auctor, nisi elit consequat ipsum...</p><a>VIEW DETAIL</a></article>
<article class="post" style="left:435px"><div class="photo" role="img" aria-label="Photo of a team working at a desk with a monitor"></div><h3>02: Some Blog Heading Here</h3><div class="meta"><span>▦ 25-05-2023</span><span>● By John</span></div><p>Aenean sollicitudin lorem quis bibendum auctor, nisi elit consequat ipsum...</p><a>VIEW DETAIL</a></article>
<article class="post" style="left:780px"><div class="photo" role="img" aria-label="Photo of a developer coding at multiple screens"></div><h3>03: Some Blog Heading Here</h3><div class="meta"><span>▦ 25-05-2023</span><span>● By John</span></div><p>Aenean sollicitudin lorem quis bibendum auctor nisi elit consequat ipsum...</p><a>VIEW DETAIL</a></article>

<!-- footer backdrop -->
<svg class="abs" style="left:0;top:3440px" width="1200" height="744" viewBox="0 0 1200 744" aria-hidden="true">
  <path d="M0,60 C150,20 250,240 500,250 C760,260 900,60 1200,90 L1200,744 L0,744 Z" fill="#4b586d"/>
  <path d="M120,250 C300,330 480,300 640,280 C820,255 980,250 1100,290" fill="none" stroke="#fff" stroke-width="14" opacity=".9"/>
</svg>

<section class="abs news">
  <h2>Subscribe Our Newsletter</h2>
  <p>Subscribe our newsletter to receive the latest news and exclusive offers every week, No spam.</p>
  <div class="email">Enter email address<span class="send"></span></div>
</section>

<div class="brand" style="left:128px;top:3864px;font-size:62px;color:#c8d1dc"><span class="dot" style="width:14px;height:14px;background:var(--yellow)"></span>Corvalin</div>
<div class="abs socials"><b></b><b></b><b></b><b></b></div>
<div class="btn btn-yellow" style="left:214px;top:4003px;width:132px;height:36px">Contact Us</div>

<div class="foot-col" style="left:491px"><h4>Quick links</h4><ul><li>Home</li><li>About Us</li><li>Services</li><li>Insights</li><li>Join Us</li><li>Contact Us</li></ul></div>
<div class="foot-col" style="left:668px"><h4>Our Services</h4><ul><li>Business Transformation</li><li>ERP Implementations</li><li>ERP Solutions</li><li>BI and Data</li><li>Building the Right Team...</li></ul></div>
<div class="foot-col" style="left:899px"><h4>Contact info</h4>
  <div class="contact-item"><svg width="13" height="10"><rect width="13" height="10" rx="1" fill="#efb81b"/></svg>Email:<br>hello@corvalinteam.com</div>
  <div class="contact-item"><svg width="13" height="13" viewBox="0 0 13 13"><path d="M3 0l2 3-1.5 1.5a8 8 0 005 5L10 8l3 2-1.5 3C6 13 0 7 0 1.5z" fill="#efb81b"/></svg>Phone:<br>+44 100 555 0190</div>
  <div class="contact-item"><svg width="11" height="14" viewBox="0 0 11 14"><path d="M5.5 0A5.5 5.5 0 000 5.5C0 9 5.5 14 5.5 14S11 9 11 5.5A5.5 5.5 0 005.5 0zm0 8a2.5 2.5 0 110-5 2.5 2.5 0 010 5z" fill="#efb81b"/></svg>Location:<br>Some address line goes<br>here city name</div>
</div>

<div class="abs bottom-bar">© Corvalin Design 2023, All Rights Reserved</div>
<div class="abs chat"></div>

</body>
</html>
```